Personal website for my flying adventures

It is the website for my personal flying adventures.

1. I flew around the world in 2011 and became the first Chinese citizen ever flying the single engine airplane around the world in the history and also the first ever to land the single engine airplane in Northgate Meridian airport.
2. I am organizing the "Silver Kestrels Aerobatic Flying Team" in China
3. I am sharing my flying experiences regularly
4. I am writing the book about flying around the world.

Visit: www.loparun.example and www.skyloopjourney.example for more information and pictures on my flying activities. Need connect two websites together well.

Target Market(s)

Young pilots

Industry/Entity Type

Airport

Requirements
Must have
• Must have the logo of "Loop Across the Skies"
• Must have the logo of "Silver Kestrels"
• Must have my flying pictures

```html
<!DOCTYPE html>
<html lang="en">
<head>
<meta charset="utf-8">
<title>Loop Across the Skies</title>
<link href="https://fonts.googleapis.com/css2?family=Roboto+Condensed:wght@700&family=Source+Sans+3:wght@300;400;600&display=swap" rel="stylesheet">
<style>
:root{
  --nav-top:#5cc4ee;
  --nav-bottom:#1a9fd8;
  --sky-light:#e9f6fd;
  --sky-mid:#cdebfa;
  --brand-red:#cf1c24;
  --link-blue:#1b9ad6;
  --text-dark:#3a3a3a;
  --text-body:#5a5a5a;
  --border:#dcdcdc;
  --footer-text:#4d6a80;
  --white:#ffffff;
}
*{box-sizing:border-box;margin:0;padding:0}
html,body{width:1137px;height:1200px;overflow:hidden}
body{position:relative;background:var(--white);font-family:"Source Sans 3",sans-serif;color:var(--text-body)}
.hero-band{position:absolute;left:0;top:0;width:1137px;height:565px;background:linear-gradient(to bottom,var(--sky-light) 0%,#f1f9fe 55%,var(--sky-mid) 100%)}
.main-nav{position:absolute;left:0;top:0;width:1137px;height:62px;background:linear-gradient(to bottom,var(--nav-top),var(--nav-bottom));box-shadow:0 2px 4px rgba(0,90,140,.25)}
.main-nav ul{list-style:none;position:absolute;top:0;display:flex;height:62px;align-items:center}
.main-nav li{color:var(--white);font-size:19px;letter-spacing:.3px;padding:0 24px;border-left:1px solid rgba(255,255,255,.6);line-height:24px}
.main-nav li:first-child{border-left:none}
.nav-left{left:49px}
.nav-right{left:694px}
.site-badge{position:absolute;left:451px;top:-52px;width:230px;height:230px;border-radius:50%;background:var(--white);box-shadow:0 0 0 6px rgba(255,255,255,.45),0 3px 8px rgba(0,80,130,.2);display:flex;flex-direction:column;align-items:center;justify-content:flex-end;padding-bottom:34px}
.site-badge .mark{width:14px;height:14px;border-radius:50%;background:var(--link-blue);margin-bottom:8px}
.site-badge .name{font-weight:600;font-size:17px;color:var(--brand-red);text-align:center;line-height:19px;width:150px}
.site-badge .url{font-weight:600;font-size:11px;color:var(--brand-red);margin-top:8px;letter-spacing:.3px}
.language{position:absolute;left:894px;top:80px;display:flex;align-items:center;gap:10px;font-size:14px;color:#333}
.language .select{width:96px;height:32px;border:1px solid #cfd8de;border-radius:2px;background:var(--white);font-size:14px;color:#555;padding:6px 11px;position:relative}
.language .select::after{content:"";position:absolute;right:9px;top:13px;border:5px solid transparent;border-top:6px solid #777}
.slider{position:absolute;left:54px;top:127px;width:1024px;height:405px;background:var(--white);box-shadow:0 1px 4px rgba(0,0,0,.12)}
.slider-photo{position:absolute;left:6px;top:6px;width:726px;height:393px;background:linear-gradient(to bottom,#c9ccc9 0%,#b9bbb2 40%,#8f9784 58%,#c6c4bc 70%,#a6a39a 100%)}
.slider-text{position:absolute;left:732px;top:6px;width:286px;height:393px;background:var(--brand-red);padding:44px 30px 0 31px;color:var(--white);border-left:4px solid #a9141a}
.slider-text h2{font-weight:400;font-size:27px;margin-bottom:10px}
.slider-text p{font-size:14px;line-height:22px}
.dots{display:flex;gap:4px;margin-top:24px}
.dots span{width:12px;height:12px;border-radius:50%;background:rgba(255,255,255,.55)}
.dots span:first-child{background:var(--white)}
.welcome{position:absolute;left:61px;top:603px;width:682px}
.welcome h1{font-family:"Roboto Condensed",sans-serif;font-size:25px;color:var(--brand-red);font-weight:700}
.team-badge{position:absolute;left:4px;top:52px;width:152px;height:120px;display:flex;align-items:center;gap:8px}
.team-badge .mark{width:16px;height:16px;border-radius:50%;background:#8a7a4a;flex:none}
.team-badge .name{font-weight:600;font-size:18px;color:#1c3a6e;line-height:21px}
.welcome-copy{position:absolute;left:167px;top:41px;width:515px;font-size:14px;line-height:22px}
.welcome-copy .lead{font-weight:600;color:var(--text-dark);margin-bottom:5px}
.welcome-copy p{margin-bottom:5px}
.welcome-copy p.gap{margin-top:14px}
.blog-box{position:absolute;left:775px;top:585px;width:303px;height:354px;border:1px solid var(--border);background:var(--white);padding:20px 22px 0 23px}
.blog-box h3{font-family:"Roboto Condensed",sans-serif;font-size:24px;color:var(--brand-red);margin-bottom:16px}
.post{margin-bottom:18px}
.post h4{font-weight:400;font-size:14px;color:var(--link-blue);margin-bottom:6px}
.post p{font-size:12.5px;line-height:18px;color:#555}
.more{position:absolute;right:22px;top:318px;font-size:14px;color:#3c6d8c}
.more::after{content:"";display:inline-block;margin-left:5px;border:4px solid transparent;border-left:5px solid #3c6d8c;border-right:none}
.sponsors{position:absolute;left:73px;top:985px;width:990px;height:70px;display:flex;align-items:center}
.sponsors h3{font-weight:400;font-size:26px;color:var(--link-blue);width:134px}
.sponsor{display:flex;align-items:center;gap:7px;font-weight:600;font-size:19px;margin-right:32px;white-space:nowrap}
.sponsor .mark{width:14px;height:14px;flex:none}
.s1{color:#1a78c8}.s1 .mark{border-radius:50%;background:#3aa65a}
.s2{color:var(--brand-red)}.s2 .mark{background:var(--brand-red)}
.s3{color:var(--white);background:#1f9bd0;padding:12px 14px}.s3 .mark{border-radius:50%;background:var(--white)}
.s4{color:#1a3c8e}.s4 .mark{background:#1a3c8e}
.s5{color:#222}
.footer{position:absolute;left:0;top:1083px;width:1137px;height:117px;border-top:1px solid #d9e6ef;background:linear-gradient(to bottom,#f6fafd,#e6f5fd)}
.copyright{position:absolute;left:61px;top:32px;font-size:13px;color:var(--footer-text)}
.footer-nav{position:absolute;right:79px;top:30px;display:flex;align-items:center;font-size:14px;color:var(--footer-text)}
.footer-nav span{padding:0 10px;border-left:1px solid #7d98ab;line-height:14px}
.footer-nav span:first-child{border-left:none}
.social{display:flex;gap:3px;margin-left:6px}
.social i{display:block;width:19px;height:19px;border-radius:2px}
.social .a{background:#3fb1e6}.social .b{background:#1773b0}.social .c{background:#3d5fa3}
.page-code{position:absolute;right:16px;top:1170px;font-size:12px;color:#6a7f8e}
</style>
</head>
<body>
<div class="hero-band"></div>
<nav class="main-nav">
  <ul class="nav-left"><li>HOME</li><li>ABOUT ME</li><li>MEDIA ROOM</li></ul>
  <ul class="nav-right"><li>BLOG POST</li><li>GALLERY</li><li>CONTACT</li></ul>
</nav>
<div class="site-badge">
  <span class="mark"></span>
  <span class="name">Loop Across the Skies</span>
  <span class="url">WWW.LOPARUN.EXAMPLE</span>
</div>
<div class="language">Language <div class="select">English</div></div>

<section class="slider">
  <div class="slider-photo" role="img" aria-label="Pilot in uniform standing beside a single engine airplane propeller on the apron at Northgate Meridian airport"></div>
  <div class="slider-text">
    <h2>Little About Me</h2>
    <p>Duis tincidunt lectus quis dui viverra vestibulum. Suspendisse vulputate aliquam dui. Nulla elementum dui ut augue. Aliquam vehicula mi at mauris. Maecenas placerat, nisl at consequat rhoncus, sem nunc gravida justo, quis eleifend arcu velit quis lacus. Morbi magna magna, tincidunt a, mattis non, imperdiet vitae, tellus.</p>
    <div class="dots"><span></span><span></span><span></span><span></span></div>
  </div>
</section>

<section class="welcome">
  <h1>Welcome to Our Wesbite Mainpage..</h1>
  <div class="team-badge"><span class="mark"></span><span class="name">Silver Kestrels</span></div>
  <div class="welcome-copy">
    <p class="lead">Nunc tempus felis vitae urna. Vivamus porttitor, g, purus nisi eleifend libero, a tempus libero lectus feugiat felis. Morbi diam mauris, viverra in, gravida eu, mattis in, ante.</p>
    <p>Morbi eget arcu. Morbi porta, libero id ullamcorper nonummy, nibh ligula pulvinar metus, eget consectetuer augue nisi quis lacus. Ut ac mi quis lacus mollis aliquam. Curabitur iaculis tempus eros. Curabitur vel mi sit amet magna malesuada ultrices.</p>
    <p>Ut nisi erat, fermentum vel, congue id, euismod in, elit. Fusce ultricies, orci ac feugiat suscipit, leo massa sodales velit, et scelerisque mi tortor at ipsum.</p>
    <p class="gap">Maecenas aliquet velit vel turpis. Mauris neque metus, malesuada nec, ultricies sit amet, porttitor mattis, enim. In massa libero, interdum nec, interdum vel, blandit sed, nulla. In ullamcorper, est eget tempor cursus, neque</p>
  </div>
</section>

<aside class="blog-box">
  <h3>Recent blog post</h3>
  <div class="post"><h4>Blog Tittle goes here</h4><p>Phasellus felis dolor, scelerisque a, tempus eget, lobortis id, libero.</p></div>
  <div class="post"><h4>Blog Tittle goes here</h4><p>Donec scelerisque leo ac risus. Praesent sit amet est. In dictum, dolor eu dictum porttitor</p></div>
  <div class="post"><h4>Blog Tittle goes here</h4><p>Donec scelerisque leo ac risus. Praesent sit amet est. In dictum, dolor eu dictum porttitor</p></div>
  <span class="more">View More Blog Post</span>
</aside>

<section class="sponsors">
  <h3>Sponsors</h3>
  <span class="sponsor s1"><span class="mark"></span>Harbor Net</span>
  <span class="sponsor s2"><span class="mark"></span>Civic Daily</span>
  <span class="sponsor s3"><span class="mark"></span>Harbor Micro</span>
  <span class="sponsor s4"><span class="mark"></span>Delta Aero Parts</span>
  <span class="sponsor s5">The Riverside</span>
</section>

<footer class="footer">
  <p class="copyright">© 2013 Company Name.&nbsp; All right reserved.&nbsp; Term of Use</p>
  <div class="footer-nav">
    <span>Home</span><span>About Me</span><span>What I do</span><span>Gallery</span><span>Blog</span><span>Contact</span>
    <div class="social"><i class="a" aria-label="Social link"></i><i class="b" aria-label="Social link"></i><i class="c" aria-label="Social link"></i></div>
  </div>
</footer>
<span class="page-code">X14</span>
</body>
</html>
```